Copper Ridge Upkeep and Errand Flyer

We need a flyer for copper ridge upkeep and errand service. We specialize in and provide residential maintenance and errand services to retired and semi retired persons living in the Lake Norman area. The services we include:
Lighting and plumbing repairs
Ceiling fan installation
Handicap accessories
Locks and security
Picture hanging
Hang blinds
Furniture arrangement / assembly
Pressure washing
Battery Jump start
and more...

Our Concierge services include:
Errand running
Grocery shopping
Wellness Checks
Dog Walk
Garbage Collection
and more...

We offer monthly service agreements and 24/7 access
Call text or e-mail for more information
555.418.2963
1copperridgeupk@quillbox-mail.net

The design should invoke a sense of trust and a customer service driven mission

Target Market(s)

Residential maintenance

Industry/Entity Type

Property Maintenance

Contact Information for Business Card

Dale Hurst
20814 Fennick Gale Rd.
Cornelius NC 28947
555.418.2963
with uploaded logo

Requirements
Nice to have
• Would like a postcard size flyer. Front and back
Should not have
• No pics of of people wearing hard hats or pics of blueprints. No pics of commercial or industrial maintenance.

```html
<!DOCTYPE html>
<html lang="en">
<head>
<meta charset="utf-8">
<title>Copper Ridge Upkeep and Errand – Postcard Flyer</title>
<link href="https://fonts.googleapis.com/css2?family=Cabin:wght@400;600;700&family=Montserrat:wght@700;800&display=swap" rel="stylesheet">
<style>
  :root{
    --brand-red:#bb2a21;
    --brand-grey:#767574;
    --logo-grey:#8a8a8a;
    --ink:#111111;
    --paper:#ffffff;
    --frame:#555555;
  }
  *{box-sizing:border-box;margin:0;padding:0}
  html,body{width:793px;height:1200px;overflow:hidden;background:var(--paper)}
  body{position:relative;font-family:"Cabin",sans-serif;color:var(--ink)}
  .side-label{position:absolute;left:0;width:793px;text-align:center;font:400 14px/1 Arial,sans-serif;color:#222}
  .side-label--front{top:0}
  .side-label--back{top:607px}

  .card{position:absolute;left:0;width:793px;height:565px;border:1px solid var(--frame);overflow:hidden;background:var(--paper)}
  .card--front{top:32px}
  .card--back{top:634px}
  .card__shapes{position:absolute;inset:0}

  .brand{position:absolute;display:flex;align-items:center;gap:12px}
  .brand__dot{width:56px;height:56px;border-radius:50%;background:var(--brand-red);flex:none}
  .brand__name{font:400 22px/1.15 "Cabin",sans-serif;color:var(--logo-grey);width:230px}
  .card--front .brand{left:28px;top:38px}
  .card--back .brand{left:40px;top:38px}

  .intro{position:absolute;left:28px;top:170px;width:290px;font-size:21px;line-height:33.5px;color:var(--paper)}
  .offer{position:absolute;left:29px;top:443px;font:800 19.5px/25.5px "Montserrat",sans-serif;color:var(--brand-red);letter-spacing:.5px;text-transform:uppercase}

  .services{position:absolute;left:400px;top:128px;width:382px;text-align:center;color:var(--paper)}
  .services__title{font-size:28.5px;font-weight:700;margin-bottom:12px}
  .services__list{list-style:none;font-size:19.5px;line-height:35.2px}

  .concierge{position:absolute;left:0;top:145px;width:396px;height:274px;background:var(--brand-red);color:var(--paper);text-align:center;padding-top:28px}
  .concierge__title{font-size:28.5px;font-weight:700;line-height:35px;margin-bottom:16px}
  .concierge__list{list-style:none;font-size:19.5px;line-height:35.5px}

  .contact{position:absolute;left:0;top:455px;width:396px;text-align:center}
  .contact__lead{font-size:17px;font-weight:700}
  .contact__phone{font:800 24px/1.2 "Montserrat",sans-serif;color:var(--brand-red);margin-top:2px}
  .contact__email{font-size:16px;font-weight:700;margin-top:1px}

  .divider{position:absolute;left:396px;top:0;width:1px;height:100%;background:var(--frame)}
  .stamp{position:absolute;left:693px;top:27px;width:64px;height:64px;border:1.5px solid var(--ink)}
</style>
</head>
<body>
  <div class="side-label side-label--front">Front</div>

  <section class="card card--front">
    <svg class="card__shapes" width="793" height="565" viewBox="0 0 793 565" aria-hidden="true">
      <rect x="0" y="146" width="340" height="274" fill="var(--brand-red)"/>
      <circle cx="545" cy="284" r="262" fill="var(--brand-grey)"/>
      <circle cx="591" cy="281" r="238" fill="var(--brand-red)"/>
    </svg>

    <div class="brand">
      <span class="brand__dot"></span>
      <span class="brand__name">Copper Ridge Upkeep and Errand</span>
    </div>

    <p class="intro">We specialize in and provide residential maintenance and errand services to retired and semi retired persons living in the Lake Norman area.</p>

    <p class="offer">We offer<br>monthly service<br>agreements and<br>24/7 access</p>

    <div class="services">
      <h2 class="services__title">The services we include:</h2>
      <ul class="services__list">
        <li>Lighting and plumbing repairs</li>
        <li>Ceiling fan installation</li>
        <li>Handicap accessories</li>
        <li>Locks and security</li>
        <li>Picture hanging | Hang blinds</li>
        <li>Furniture arrangement / assembly</li>
        <li>Pressure washing | Battery Jump start</li>
        <li>and more...</li>
      </ul>
    </div>
  </section>

  <div class="side-label side-label--back">Back</div>

  <section class="card card--back">
    <div class="brand">
      <span class="brand__dot"></span>
      <span class="brand__name">Copper Ridge Upkeep and Errand</span>
    </div>

    <div class="concierge">
      <h2 class="concierge__title">Our Concierge<br>services include:</h2>
      <ul class="concierge__list">
        <li>Errand running | Grocery shopping</li>
        <li>Wellness Checks | Dog Walk</li>
        <li>Garbage Collection</li>
        <li>and more...</li>
      </ul>
    </div>

    <div class="contact">
      <p class="contact__lead">Call text or e-mail for more information</p>
      <p class="contact__phone">555.418.2963</p>
      <p class="contact__email">1copperridgeupk@quillbox-mail.net</p>
    </div>

    <div class="divider"></div>
    <div class="stamp" aria-label="Stamp area"></div>
  </section>
</body>
</html>
```